Second-Line Parade Announcement

Many members of our local chapter will be heading to New Orleans, LA, USA, in March 2019 to attend a large event hosted by our parent company. As part of this trip, we're hosting our own parade in The French Quarter (famous area of New Orleans), and we want to advertise this particular event, along with 1-2 others, on a one-page flyer.

This should be an invitation. What we're hosting is a "second-line parade," which is a much smaller, personal parade (not like big street parades), usually with 10-20 people.

Target Market(s)

Our own members

Colors

Designer to choose colors to be used in the design.

Requirements
Must have
• - Time & date (4:45 p.m., Sunday, March 17, 2019) and location (French Quarter)
• - Please include imagery of a New-Orleans-style parade (with traditional brass band) *OR* imagery of horn musicians (trumpeter, trombonist, etc.). It does not need to be a photo...could be an illustration...attached some for inspiration
• Final deliverable MUST include designer's raw files (e.g., .AI, .IDML, .PSD, etc.)
Nice to have
• I have included ads from our parent organization for the big conference, which can be used as part of your design or simply as inspiration for your design. I have also enclosed some sketch-like images of musicians that I don't own but that could be used as inspiration.
Should not have
• Please avoid imagery of alcohol, leprechauns (although a tasteful "leprechaun-style" hat would be okay), money/pots of gold and anything 'cartoon-like' or 'child-like.'
• Please leave some room ("white space") for additional details/instructions as they might arise.

```html
<!DOCTYPE html>
<html lang="en">
<head>
<meta charset="utf-8">
<title>Second-Line Parade Invitation</title>
<link rel="stylesheet" href="https://fonts.googleapis.com/css2?family=Open+Sans:wght@800&family=Lato:wght@400;700;900&family=Yellowtail&display=swap">
<style>
  :root {
    --stage: #d9d9d6;
    --green-deep: #0c220e;
    --green-mid: #1d4a1f;
    --green-glow: #3c8a2e;
    --accent: #8cc63f;
    --frame: #4aa63a;
    --white: #ffffff;
    --silver: #d8dcd8;
    --gold: #d9b24a;
  }
  * { margin: 0; padding: 0; box-sizing: border-box; }
  html, body {
    width: 1200px; height: 964px; overflow: hidden;
    background: var(--stage);
  }
  .flyer {
    position: absolute; left: 270px; top: 32px;
    width: 660px; height: 900px; overflow: hidden;
    background: radial-gradient(ellipse at 50% 40%, var(--green-mid) 0%, #163a18 45%, var(--green-deep) 100%);
    box-shadow: 0 6px 24px rgba(0,0,0,.25);
    font-family: "Lato", sans-serif; color: var(--white);
  }
  .string-lights {
    position: absolute; left: 0; top: 0; width: 660px; height: 90px;
    background: linear-gradient(180deg, rgba(90,170,80,.18), rgba(90,170,80,0));
  }
  .title-frame {
    position: absolute; left: 78px; top: 118px; width: 504px; height: 150px;
    border: 2px solid var(--frame);
  }
  .title-script {
    position: absolute; font-family: "Yellowtail", cursive; color: var(--accent);
    font-size: 40px; line-height: 1; padding: 0 10px;
    background: #17401a;
  }
  .title-script.happy { left: 250px; top: 96px; }
  .title-script.day { left: 330px; top: 248px; background: #194419; }
  .title-main {
    position: absolute; left: 0; width: 660px; top: 140px; text-align: center;
    font-family: "Open Sans", sans-serif; font-weight: 800; font-size: 92px;
    letter-spacing: 1px; line-height: 1;
    background: linear-gradient(180deg, var(--white) 30%, var(--silver));
    -webkit-background-clip: text; background-clip: text; color: transparent;
  }
  .hat-art {
    position: absolute; left: 110px; top: 300px; width: 440px; height: 270px;
    border-radius: 50% 50% 45% 45% / 40% 40% 60% 60%;
    background: radial-gradient(ellipse at 50% 45%, #6fd04a 0%, var(--green-glow) 45%, rgba(30,80,30,0) 72%);
  }
  .invite-script {
    position: absolute; left: 0; width: 660px; top: 590px; text-align: center;
    font-family: "Yellowtail", cursive; font-size: 46px; line-height: 1;
  }
  .event-name {
    position: absolute; left: 0; width: 660px; top: 640px; text-align: center;
    font-family: "Open Sans", sans-serif; font-weight: 800; font-size: 58px;
    line-height: 1; letter-spacing: .5px;
  }
  .details {
    position: absolute; left: 40px; right: 40px; top: 748px;
    display: flex; align-items: flex-start; gap: 22px;
  }
  .host {
    display: flex; align-items: center; gap: 12px; padding-top: 6px;
    width: 210px;
  }
  .host-dot {
    flex: none; width: 46px; height: 46px; border-radius: 50%;
    background: var(--accent);
  }
  .host-name { font-size: 18px; font-weight: 400; line-height: 1.15; color: var(--white); }
  .divider { width: 2px; height: 74px; background: var(--accent); flex: none; }
  .info-label { color: var(--accent); font-weight: 900; font-size: 18px; margin-bottom: 4px; }
  .info-text { font-weight: 900; font-size: 18px; line-height: 1.2; }
  .info.when { width: 170px; }
  .info.where { width: 140px; margin-top: 20px; }
  .divider.second { margin-top: 20px; }
</style>
</head>
<body>
  <main class="flyer">
    <div class="string-lights" role="img" aria-label="Glowing string of green party lights"></div>

    <div class="title-frame"></div>
    <div class="title-main">PATRICK´S</div>
    <span class="title-script happy">Happy St.</span>
    <span class="title-script day">Day</span>

    <div class="hat-art" role="img" aria-label="Glowing green top hat with a gold buckle and shamrock, gold coins and grass"></div>

    <p class="invite-script">an Invitation</p>
    <h1 class="event-name">SECOND-LINE PARADE</h1>

    <section class="details">
      <div class="host">
        <span class="host-dot"></span>
        <span class="host-name">Hudson Valley Heart Society</span>
      </div>
      <span class="divider"></span>
      <div class="info when">
        <p class="info-label">Time &amp; Date:</p>
        <p class="info-text">4:45 p.m., Sunday,<br>March 17, 2019</p>
      </div>
      <span class="divider second"></span>
      <div class="info where">
        <p class="info-label">Location:</p>
        <p class="info-text">French<br>Quarter</p>
      </div>
    </section>
  </main>
</body>
</html>
```